I already have a business sign that has what I want on my business cards, however it needs to be modified to make a double sided business card. Also the wording needs modification. I want the Corvella Tennis Coaching logo on the front of the business card with the Black/Green background. And I want the tennis ball dot points on the back of the card with the green background. The dot points as follows:
-All Ages Welcome
-Qualified, Enthusiastic Coaches
-Group, Semi Private & Private Lessons
-Beginner, Intermediate and Advanced Standards
-Velmora Rally
-Kestrel Kids

Also, I want the "A GREAT WAY TO GET FIT AND HEALTHY" to remain as is, and my name and number.
I've added a file that has my current signage, as a guide.

```html
<!DOCTYPE html>
<html lang="en">
<head>
<meta charset="utf-8">
<title>Corvella Tennis Coaching – Business Card</title>
<link rel="stylesheet" href="https://fonts.googleapis.com/css2?family=Exo+2:wght@400;800&family=Russo+One&display=swap">
<style>
  :root {
    --page-bg: #d9d9d9;
    --card-border: #ffffff;
    --charcoal: #231f20;
    --court-green: #004a1f;
    --ball-yellow: #a9c93a;
    --text-light: #ffffff;
    --name-dark: #1c1c1c;
  }
  * { margin: 0; padding: 0; box-sizing: border-box; }
  html, body { width: 1200px; height: 1000px; overflow: hidden; }
  body { background: var(--page-bg); position: relative; font-family: "Exo 2", sans-serif; }

  .card { position: absolute; left: 250px; width: 700px; height: 400px; background: var(--card-border); }
  .card-front { top: 106px; height: 399px; }
  .card-back { top: 530px; }

  .front-face {
    position: absolute; left: 20px; top: 20px; width: 660px; height: 359px;
    background: var(--charcoal); border-radius: 14px;
    display: flex; align-items: center; justify-content: center; gap: 22px;
  }
  .brand-dot { width: 64px; height: 64px; border-radius: 50%; background: var(--ball-yellow); flex: none; }
  .brand-name { color: var(--text-light); font-weight: 800; font-size: 42px; letter-spacing: 0.5px; }

  .back-face {
    position: absolute; left: 20px; top: 20px; width: 660px; height: 360px;
    background: var(--court-green); border-radius: 0 14px 14px 0; overflow: hidden;
  }
  .back-face .side-band { position: absolute; left: 0; top: 0; width: 150px; height: 360px; }
  .tagline {
    position: absolute; left: 0; top: 118px; width: 118px;
    font-family: "Russo One", sans-serif; color: var(--text-light);
    font-size: 21px; line-height: 29px; text-align: center; text-transform: uppercase;
  }

  .feature { position: absolute; color: var(--text-light); font-size: 21px; line-height: 26px; letter-spacing: 0.4px; }
  .ball { position: absolute; width: 34px; height: 34px; }

  .owner-name {
    position: absolute; left: 172px; top: 280px;
    font-family: "Russo One", sans-serif; font-size: 44px; color: var(--name-dark); letter-spacing: 1px;
  }
  .owner-phone {
    position: absolute; left: 398px; top: 324px;
    font-family: "Russo One", sans-serif; font-size: 28px; color: var(--text-light); letter-spacing: 0.5px;
  }
</style>
</head>
<body>

<section class="card card-front">
  <div class="front-face">
    <span class="brand-dot"></span>
    <span class="brand-name">Corvella Tennis Coaching</span>
  </div>
</section>

<section class="card card-back">
  <div class="back-face">
    <svg class="side-band" viewBox="0 0 150 360" aria-hidden="true">
      <polygon points="0,0 118,0 118,275 150,305 118,335 118,360 0,360" fill="var(--charcoal)"/>
    </svg>
    <p class="tagline">A great way to get fit and healthy</p>

    <svg style="display:none" aria-hidden="true">
      <symbol id="tennis-ball" viewBox="0 0 34 34">
        <circle cx="17" cy="17" r="16" fill="#ffffff"/>
        <path d="M9 4 C17 10 17 24 9 30" fill="none" stroke="#9a9a9a" stroke-width="2"/>
      </symbol>
    </svg>

    <svg class="ball" style="left:125px;top:11px"><use href="#tennis-ball"/></svg>
    <p class="feature" style="left:181px;top:22px">All Ages Welcome</p>

    <svg class="ball" style="left:412px;top:38px"><use href="#tennis-ball"/></svg>
    <p class="feature" style="left:487px;top:32px">Velmora Rally</p>

    <svg class="ball" style="left:123px;top:84px"><use href="#tennis-ball"/></svg>
    <p class="feature" style="left:178px;top:82px">Beginner, Intermediate and<br>Advanced Standards</p>

    <svg class="ball" style="left:424px;top:124px"><use href="#tennis-ball"/></svg>
    <p class="feature" style="left:498px;top:133px">Kestrel Kids</p>

    <svg class="ball" style="left:127px;top:166px"><use href="#tennis-ball"/></svg>
    <p class="feature" style="left:180px;top:172px">Group, Semi Private &amp; Private Lessons</p>

    <svg class="ball" style="left:143px;top:226px"><use href="#tennis-ball"/></svg>
    <p class="feature" style="left:198px;top:226px">Qualified, Enthusiastic Coaches</p>

    <p class="owner-name">DANE WHITCOMBE</p>
    <p class="owner-phone">0491 570 236</p>
  </div>
</section>

</body>
</html>
```